Newspaper AD in the Restaurant Section HOMECARE/Senior Living

Looking for an ad that is 6.425 inches wide and 5 inches tall to go into the newspaper weekly it will be in the restaurant section. We are a senior homecare company and we are looking to show clients that caregivers are able to assist them not only in personal care needs but also meal prep. We would like the design to have the feel of our existing ad or our newly launched website. It will be in the Savor section of the Pacific Morning Ledger which is not where we normally would advertise as a homecare agency so ad has to have some kind of feel for that section.
It should say somewhere maybe by contact info Call today for FREE Consultation.

Target Market(s)

Target market is Men/Women ages 35-105

Industry/Entity Type

Homecare and Senior Living

Font styles to use
Sans Serif

Colors
0054AA
0677BA
7BADD7
CADEEF
E8F1F8
FFF300
FFF600
FEFA6F
FFFEC7
FFFEE8
EB3D1F
EC4F4E
F09395
F8D3D4
FCEDEE

Requirements
Must have
• Logo, Contact info: Phone number (808) 555-0173, email address Info@brightmeadowcare.com and website www.Brightmeadowcare.com.
Nice to have
• Something that will be eye catching and to the point. Maybe a picture of a caregiver preparing a meal with an elderly person

```html
<!DOCTYPE html>
<html lang="en">
<head>
<meta charset="utf-8">
<title>Brightmeadow Homecare – Newspaper Ad</title>
<link rel="stylesheet" href="https://fonts.googleapis.com/css2?family=Roboto+Slab:wght@600;700&family=Poppins:wght@500&family=Playfair+Display:ital,wght@0,400;1,700&display=swap">
<style>
  :root {
    --page: #e4e4e4;
    --green-dark: #0c5249;
    --green: #0f6356;
    --salmon: #f0907a;
    --salmon-soft: #f3a18c;
    --white: #ffffff;
    --black: #0b0b0b;
    --photo-warm: #9a5a3a;
    --photo-light: #d8c7a8;
  }
  html, body {
    margin: 0;
    width: 1200px;
    height: 800px;
    overflow: hidden;
    background: var(--page);
  }
  .ad {
    position: absolute;
    left: 86px;
    top: 0;
    width: 1028px;
    height: 800px;
    overflow: hidden;
  }
  .ad-shapes {
    position: absolute;
    inset: 0;
  }
  .brand {
    position: absolute;
    left: 172px;
    top: 100px;
    width: 200px;
    text-align: center;
  }
  .brand-mark {
    display: block;
    width: 96px;
    height: 96px;
    margin: 0 auto 22px;
    border-radius: 12px;
    background: var(--salmon);
  }
  .brand-name {
    font-family: "Roboto Slab", serif;
    font-weight: 600;
    color: var(--salmon);
    font-size: 36px;
    line-height: 1.15;
    margin: 0;
    letter-spacing: 0.5px;
  }
  .headline {
    position: absolute;
    left: 72px;
    top: 398px;
    margin: 0;
    font-family: "Roboto Slab", serif;
    font-weight: 700;
    font-size: 51px;
    line-height: 64px;
    color: var(--white);
  }
  .headline .accent { color: var(--salmon); }
  .contact {
    position: absolute;
    left: 72px;
    top: 626px;
    margin: 0;
    padding: 0;
    list-style: none;
    font-family: "Poppins", sans-serif;
    font-weight: 500;
    font-size: 20px;
    letter-spacing: 1.4px;
    color: var(--white);
  }
  .contact li {
    display: flex;
    align-items: center;
    height: 44px;
  }
  .contact svg { width: 31px; height: 31px; margin-right: 11px; flex: none; }
  .contact .upper { text-transform: uppercase; }
  .offer {
    position: absolute;
    left: 794px;
    top: 641px;
    width: 171px;
    height: 159px;
    text-align: center;
    color: var(--white);
  }
  .offer svg { position: absolute; inset: 0; }
  .offer-big {
    position: relative;
    display: block;
    padding-top: 34px;
    font-family: "Playfair Display", serif;
    font-style: italic;
    font-weight: 700;
    font-size: 52px;
    line-height: 56px;
  }
  .offer-small {
    position: relative;
    display: block;
    font-family: "Playfair Display", serif;
    font-size: 25px;
    line-height: 28px;
  }
</style>
</head>
<body>
<main class="ad">
  <svg class="ad-shapes" viewBox="0 0 1028 800" width="1028" height="800" aria-hidden="false">
    <defs>
      <linearGradient id="greenFill" x1="0" y1="0" x2="0.6" y2="1">
        <stop offset="0" stop-color="var(--green-dark)"/>
        <stop offset="1" stop-color="var(--green)"/>
      </linearGradient>
      <linearGradient id="photoFill" x1="0" y1="0" x2="1" y2="1">
        <stop offset="0" stop-color="var(--photo-warm)"/>
        <stop offset="0.55" stop-color="#b88562"/>
        <stop offset="1" stop-color="var(--photo-light)"/>
      </linearGradient>
    </defs>
    <rect class="salmon-field" width="1028" height="800" fill="var(--salmon-soft)"/>
    <path class="green-field" d="M0 0 H780 L830 420 C750 560 690 690 618 800 H0 Z" fill="url(#greenFill)"/>
    <ellipse class="photo-rim" cx="894" cy="40" rx="425" ry="392" fill="var(--white)"/>
    <ellipse class="photo-area" role="img" aria-label="Photo: a caregiver in scrubs serving a meal to an older couple seated at a kitchen table" cx="900" cy="30" rx="412" ry="377" fill="url(#photoFill)"/>
  </svg>

  <div class="brand">
    <span class="brand-mark"></span>
    <p class="brand-name">Brightmeadow<br>Homecare</p>
  </div>

  <h1 class="headline">
    Caregivers <span class="accent">Not Only</span><br>
    <span class="accent">In Personal Care</span> Needs But<br>
    Also Meal Preparation!
  </h1>

  <ul class="contact">
    <li>
      <svg viewBox="0 0 32 32"><circle cx="16" cy="16" r="15" fill="var(--salmon)"/><path d="M11 8.5c1-.6 1.8-.3 2.3.6l1.4 2.6c.4.8.2 1.5-.5 2l-1 .8c.8 1.9 2.3 3.4 4.2 4.3l.8-1c.5-.7 1.3-.9 2-.5l2.6 1.4c.9.5 1.2 1.3.6 2.3-.9 1.4-2.3 2.1-3.9 1.6-4.4-1.4-7.7-4.7-9.1-9.1-.5-1.6.2-3 1.6-3.9z" fill="var(--green-dark)"/></svg>
      <span>(808) 555-0173</span>
    </li>
    <li>
      <svg viewBox="0 0 32 32"><circle cx="16" cy="16" r="15" fill="var(--salmon)"/><rect x="8.5" y="10.5" width="15" height="11" rx="1.5" fill="none" stroke="var(--green-dark)" stroke-width="1.8"/><path d="M9 11.5l7 5.5 7-5.5" fill="none" stroke="var(--green-dark)" stroke-width="1.8"/></svg>
      <span class="upper">Info@brightmeadowcare.com</span>
    </li>
    <li>
      <svg viewBox="0 0 32 32"><circle cx="16" cy="16" r="15" fill="var(--salmon)"/><g fill="none" stroke="var(--green-dark)" stroke-width="1.6"><circle cx="16" cy="16" r="8"/><ellipse cx="16" cy="16" rx="3.5" ry="8"/><path d="M8 16h16M9.2 12h13.6M9.2 20h13.6"/></g></svg>
      <span class="upper">www.Brightmeadowcare.com</span>
    </li>
  </ul>

  <div class="offer">
    <svg viewBox="0 0 171 159" width="171" height="159" aria-hidden="true"><path d="M0 0 L85.5 14 L171 0 V159 H0 Z" fill="var(--black)"/></svg>
    <span class="offer-big">FREE</span>
    <span class="offer-small">Consultation</span>
  </div>
</main>
</body>
</html>
```